Strength and Conditioning Business needs a logo design

We need a logo design for a fitness company based in South Carolina called "K7R Motion Dynamics". We are a group of Strength and Conditioning Coaches that work with youth, high school, collegiate, and professional athletes. We also train general population clients that are looking to improve their overall fitness. Our primary mission is to make sure our athletes are able to gain the greatest benefits from training that will allow them to excel in their sport. We use heavy chains, kettle bells, resistance bands, dumbbells, prowlers (sleds), and multi-functional machines for training. We have a dynamic and collaborative approach that utilizes high-intensity intervals combined with speed, power, agility, and strength training.

Industry/Entity Type

Fitness

Contact Information for Business Card

K7R Motion Dynamics
Lorenzo Baptiste, MEd, CPT, PES
Head of Athlete Development
Brookhaven, SC
Phone: (555) 318-7046
Email: k7rmotiondynamics@quikmailbox.net
Instagram: lift_mentor_lb

Font styles to use
Sans Serif

Colors
9bcb3c
ffffff
000000
474747
ec1f27
7f7f7f
0456a4

Requirements
Must have
• I would like to have a black card with either lime green or bold blue accents along with white and silver. On the back, I would like the name 'K7R Motion Dynamics' with a subheading that says, 'Strength and Conditioning.'
Nice to have
• I really like the designs of the cards I uploaded. For the logo, something clean, bold, and eye-catching would be great.
Should not have
• I do not want a logo that will make it difficult to read.

```html
<!DOCTYPE html>
<html lang="en">
<head>
<meta charset="utf-8">
<title>K7R Motion Dynamics – Business Card</title>
<link href="https://fonts.googleapis.com/css2?family=Montserrat:wght@500;800&family=Oswald:wght@400;500&display=swap" rel="stylesheet">
<style>
  :root {
    --lime: #9bcb3c;
    --white: #ffffff;
    --silver: #e3e3e3;
    --card: #1e1e1e;
    --backdrop: #d9d9d6;
  }
  * { margin: 0; padding: 0; box-sizing: border-box; }
  html, body { width: 1200px; height: 900px; overflow: hidden; background: var(--backdrop); }
  .canvas { position: relative; width: 1200px; height: 900px; }

  .card {
    position: absolute; left: 250px; width: 700px; height: 400px;
    background: var(--card); border-radius: 4px;
    box-shadow: 0 6px 18px rgba(0,0,0,.25);
    overflow: hidden;
  }
  .card--front { top: 30px; display: flex; flex-direction: column; align-items: center; justify-content: center; padding-bottom: 30px; }
  .card--contact { top: 470px; }

  .brand-name {
    font-family: "Montserrat", sans-serif; font-weight: 800;
    color: var(--silver); text-transform: uppercase; letter-spacing: 2px; line-height: 1.05;
    text-align: center;
  }
  .brand-name span { display: block; }
  .card--front .brand-name { font-size: 58px; }

  .tagline {
    display: flex; align-items: center; gap: 10px; margin-top: 16px;
    font-family: "Montserrat", sans-serif; font-weight: 500;
    color: var(--lime); text-transform: uppercase; letter-spacing: 1.5px; white-space: nowrap;
  }
  .tagline::before, .tagline::after { content: ""; height: 1.5px; background: var(--lime); }
  .card--front .tagline { font-size: 17px; }
  .card--front .tagline::before, .card--front .tagline::after { width: 60px; }

  .logo-block {
    position: absolute; left: 30px; top: 140px; width: 280px;
    display: flex; flex-direction: column; align-items: center;
  }
  .logo-block .brand-name { font-size: 30px; letter-spacing: 1.5px; }
  .logo-block .tagline { font-size: 9.5px; margin-top: 10px; gap: 6px; letter-spacing: 1px; }
  .logo-block .tagline::before, .logo-block .tagline::after { width: 24px; }

  .divider { position: absolute; left: 336px; top: 62px; width: 3px; height: 280px; background: var(--lime); }

  .contact { position: absolute; left: 356px; top: 60px; font-family: "Oswald", sans-serif; color: var(--white); }
  .contact__name { font-size: 30px; font-weight: 500; color: var(--lime); text-transform: uppercase; line-height: 1.1; }
  .contact__role { font-size: 20px; line-height: 1.4; }
  .contact__list { list-style: none; margin-top: 38px; }
  .contact__item { display: flex; align-items: center; gap: 10px; font-size: 22px; height: 42px; white-space: nowrap; }
  .contact__item--email { font-size: 20px; }
  .icon { width: 30px; height: 30px; flex: none; }
</style>
</head>
<body>
<main class="canvas">
  <section class="card card--front" aria-label="Card front">
    <h1 class="brand-name"><span>K7R Motion</span><span>Dynamics</span></h1>
    <p class="tagline">Strength and Conditioning</p>
  </section>

  <section class="card card--contact" aria-label="Card contact side">
    <div class="logo-block">
      <p class="brand-name"><span>K7R Motion</span><span>Dynamics</span></p>
      <p class="tagline">Strength and Conditioning</p>
    </div>
    <div class="divider"></div>
    <div class="contact">
      <h2 class="contact__name">Lorenzo Baptiste</h2>
      <p class="contact__role">MEd, CPT, PES<br>Head of Athlete Development<br>Brookhaven, SC</p>
      <ul class="contact__list">
        <li class="contact__item">
          <svg class="icon" viewBox="0 0 30 30" aria-hidden="true"><circle cx="15" cy="15" r="15" fill="#9bcb3c"/><path d="M10 8.5c1-.6 1.8-.4 2.3.4l1.2 2.2c.4.7.2 1.4-.4 1.9l-.8.6c.7 1.7 2 3 3.6 3.8l.7-.8c.5-.6 1.3-.7 1.9-.3l2.1 1.3c.8.5 1 1.3.4 2.2-1.1 1.7-3 2-5 1-3.2-1.6-5.6-4.3-6.8-7.5-.7-2-.3-3.8.8-4.8z" fill="#1e1e1e"/></svg>
          (555) 318-7046
        </li>
        <li class="contact__item contact__item--email">
          <svg class="icon" viewBox="0 0 30 30" aria-hidden="true"><circle cx="15" cy="15" r="15" fill="#9bcb3c"/><rect x="8" y="10" width="14" height="10" fill="#1e1e1e"/><path d="M8 10l7 6 7-6" fill="none" stroke="#9bcb3c" stroke-width="1.3"/></svg>
          k7rmotiondynamics@quikmailbox.net
        </li>
        <li class="contact__item">
          <svg class="icon" viewBox="0 0 30 30" aria-hidden="true"><circle cx="15" cy="15" r="15" fill="#9bcb3c"/></svg>
          lift_mentor_lb
        </li>
      </ul>
    </div>
  </section>
</main>
</body>
</html>
```